Company or website name
- zestoplex
- Links to the website
- www.zestoplex.com
- Describe your company and organization and target audience
- I need a website design for a new kids vitamins brand called ZESTOPLEX.   This brand is built on the foundations that it has everything you need, nothing that you dont (e.g. GMO, Animal Content, Soy, Dairy, Gelatin) and is right for everyone. This is a brand that appeals to millenial moms who want only the best for their kids.  It's colorful, bold, vibrant yet credible because all formulas are clinically tested.
- Other Facts

```html
<!DOCTYPE html>
<html lang="en">
<head>
<meta charset="utf-8">
<title>Zestoplex – Kids Vitamins</title>
<link href="https://fonts.googleapis.com/css2?family=Poppins:wght@400;500;600&display=swap" rel="stylesheet">
<style>
  :root{
    --pink:#e5679f;
    --purple:#a070c0;
    --violet:#b477c9;
    --red:#e8473f;
    --orange:#f07a3a;
    --white:#ffffff;
  }
  *{box-sizing:border-box;margin:0;padding:0}
  html,body{width:674px;height:1200px;overflow:hidden;background:var(--white)}
  body{font-family:"Poppins",sans-serif;color:var(--pink)}
  a{text-decoration:none}
  .page{position:relative;width:674px;height:1200px;overflow:hidden;background:var(--white)}
  .layer{position:absolute;left:0;top:0}
  .abs{position:absolute}

  .nav{position:absolute;top:26px;left:330px;display:flex;align-items:center;font-size:10px;color:var(--white)}
  .nav a{color:var(--white);display:block;padding:5px 13px;line-height:13px}
  .nav a.active{border:1px solid var(--white);border-radius:12px;padding:5px 12px}
  .nav .login::before{content:"";display:inline-block;border-left:6px solid var(--white);border-top:4px solid transparent;border-bottom:4px solid transparent;margin-right:4px}

  .brand{left:66px;top:55px;font-size:18px;font-weight:600;letter-spacing:.5px;color:var(--pink)}
  .hero-title{left:64px;top:120px;font-size:26px;font-weight:500;line-height:31px;color:var(--pink)}
  .hero-copy{left:66px;top:192px;width:210px;font-size:6.6px;line-height:8.4px;color:var(--pink)}

  .hero-art{left:396px;top:72px;width:230px;height:186px;border-radius:40% 46% 42% 48%;
    background:linear-gradient(160deg,#d39a5e 0%,#c98a4c 50%,#e06a6a 100%);opacity:.9}

  .about-title{left:66px;top:314px;font-size:25px;font-weight:500;line-height:29px;color:var(--white)}
  .pill{display:inline-block;border:1px solid var(--white);border-radius:12px;color:var(--white);font-size:9px;padding:4px 11px}
  .about-more{left:66px;top:381px}
  .about-copy{left:277px;top:358px;width:143px;font-size:6.6px;line-height:8.6px;color:var(--white)}
  .tagline{right:65px;top:383px;text-align:right;font-size:26px;font-weight:500;line-height:29px;color:var(--white)}
  .tag-more{right:66px;top:479px}

  .product-title{left:66px;top:480px;font-size:26px;font-weight:500;color:var(--pink);line-height:31px}
  .product-copy{left:66px;top:519px;width:190px;font-size:6.6px;line-height:8.6px;color:var(--pink)}

  .lineup{left:89px;top:562px;width:511px;height:204px;border-radius:30px 30px 14px 14px;
    background:linear-gradient(90deg,#7fc9e0 0%,#b59ad6 18%,#f3b0d3 34%,#ef6b6b 50%,#f39a5a 66%,#f5c95b 82%,#5fc79c 100%);opacity:.85}

  .flavour-card{left:0;top:773px;width:218px;height:132px;border-radius:0 22px 22px 0;
    background:linear-gradient(135deg,#f2574a 0%,#ee6c5c 45%,#b071c0 100%);padding:22px 0 0 66px;color:var(--white)}
  .flavour-card .kicker{font-size:7px;line-height:9px}
  .flavour-card h3{font-size:21px;font-weight:500;line-height:24px;margin-top:5px}
  .flavour-card p{font-size:6.6px;line-height:8.4px;margin-top:7px;width:140px}

  .flavour-name{left:277px;top:792px;font-size:18px;font-weight:600;color:var(--red);letter-spacing:.5px}
  .buy{left:303px;top:834px;width:86px;height:32px;border-radius:8px;background:var(--red);color:var(--white);font-size:12px;font-weight:500;display:flex;align-items:center;justify-content:center}

  .contact{color:var(--white)}
  .contact .main{font-size:12.5px;font-weight:500;line-height:15px}
  .contact .sub{font-size:5.6px;line-height:8px;font-weight:500}
  .phone{left:110px;top:1070px}
  .mail{left:110px;top:1117px}
  .footer-brand{left:459px;top:1122px;color:var(--white);text-align:center}
  .footer-brand .name{font-size:15px;font-weight:600;letter-spacing:.5px;line-height:18px}
  .footer-brand .url{font-size:9px;line-height:11px;font-weight:500}
  .footer-mark{left:588px;top:1124px;width:18px;height:18px;border-radius:50%;background:#d89046}
</style>
</head>
<body>
<main class="page">

  <svg class="layer" width="674" height="1200" viewBox="0 0 674 1200" aria-hidden="true">
    <defs>
      <linearGradient id="heroGrad" x1="0" y1="0" x2="1" y2="1">
        <stop offset="0" stop-color="#f29ac0"/>
        <stop offset=".55" stop-color="#d47ab9"/>
        <stop offset="1" stop-color="#a46cc4"/>
      </linearGradient>
      <linearGradient id="bandGrad" x1="0" y1="0" x2="1" y2="0">
        <stop offset="0" stop-color="#f8a37a"/>
        <stop offset=".45" stop-color="#ee86a4"/>
        <stop offset="1" stop-color="#c97ac0"/>
      </linearGradient>
      <linearGradient id="footGrad" x1="0" y1="0" x2="1" y2="0">
        <stop offset="0" stop-color="#a870c6"/>
        <stop offset=".5" stop-color="#d77fb6"/>
        <stop offset="1" stop-color="#f2a0b8"/>
      </linearGradient>
    </defs>

    <path d="M305 0 H674 V285 C620 300 560 292 515 268 C470 244 450 190 420 140 C390 92 330 70 312 40 Z" fill="url(#heroGrad)"/>
    <path d="M300 110 C300 70 360 62 410 78 C460 94 470 150 440 190 C410 225 350 215 320 185 C302 165 300 140 300 110 Z" fill="#8fd3e3" opacity=".85"/>
    <path d="M355 225 C350 180 410 160 470 175 C530 190 565 225 560 262 C552 292 490 296 440 288 C390 280 360 258 355 225 Z" fill="#f8e27a" opacity=".9"/>
    <circle cx="409" cy="91" r="11" fill="#f3ef9e" opacity=".8"/>
    <circle cx="601" cy="104" r="4" fill="#f8e27a"/>

    <path d="M0 254 Q0 240 14 243 L660 372 Q674 375 674 390 L674 532 Q674 546 660 544 L14 443 Q0 441 0 428 Z" fill="url(#bandGrad)"/>

    <g opacity=".55">
      <circle cx="20" cy="300" r="18" fill="#f47f7a"/>
      <circle cx="45" cy="428" r="10" fill="#f3b0d0"/>
      <circle cx="0" cy="478" r="24" fill="#fbc79f"/>
      <circle cx="640" cy="360" r="28" fill="#bfe6f2"/>
      <circle cx="585" cy="352" r="9" fill="#9fd8ee"/>
      <circle cx="655" cy="480" r="22" fill="#d26aa9"/>
      <circle cx="620" cy="412" r="10" fill="#b266b8"/>
      <circle cx="640" cy="616" r="17" fill="#f6b7d4"/>
      <circle cx="660" cy="730" r="22" fill="#fbc79f"/>
      <circle cx="609" cy="776" r="14" fill="#b9b0e3"/>
      <circle cx="650" cy="822" r="14" fill="#a7dcc3"/>
      <circle cx="540" cy="835" r="17" fill="#fbc79f"/>
      <circle cx="582" cy="833" r="8" fill="#c9e8b9"/>
      <circle cx="630" cy="880" r="16" fill="#f5a6b3"/>
      <circle cx="50" cy="697" r="14" fill="#f5a6b3"/>
      <circle cx="18" cy="672" r="8" fill="#f8e27a"/>
      <circle cx="3" cy="617" r="13" fill="#b9b0e3"/>
      <circle cx="32" cy="912" r="12" fill="#d9efc6"/>
    </g>

    <circle cx="206" cy="803" r="2" fill="#e8473f"/>
    <line x1="212" y1="803" x2="258" y2="803" stroke="#e8473f" stroke-width="1.5" stroke-dasharray="6 5"/>
    <path d="M262 800 L256 803 L262 806" fill="none" stroke="#e8473f" stroke-width="1.5"/>

    <path d="M265 850 L278 838 V845 H292 V855 H278 V862 Z" fill="#b477c9"/>
    <path d="M430 850 L417 838 V845 H402 V855 H417 V862 Z" fill="#f07a3a"/>

    <g stroke="#fff" stroke-width="1.5" fill="none">
      <circle cx="171" cy="961" r="25" fill="#2bb38a"/><circle cx="171" cy="961" r="20"/>
      <circle cx="230" cy="961" r="25" fill="#f4b51c"/><circle cx="230" cy="961" r="20"/>
      <circle cx="289" cy="961" r="25" fill="#1aa2b8"/><circle cx="289" cy="961" r="20"/>
      <circle cx="348" cy="961" r="25" fill="#6d5aa8"/><circle cx="348" cy="961" r="20"/>
      <circle cx="406" cy="961" r="25" fill="#b6519a"/><circle cx="406" cy="961" r="20"/>
      <circle cx="464" cy="961" r="25" fill="#ee7a2f"/><circle cx="464" cy="961" r="20"/>
      <circle cx="521" cy="961" r="25" fill="#e44a55"/><circle cx="521" cy="961" r="20"/>
    </g>

    <path d="M0 1040 C110 1010 230 1010 330 1040 C450 1075 560 1060 674 1015 V1200 H0 Z" fill="url(#footGrad)"/>
    <path d="M0 1170 C120 1150 220 1160 330 1185 C360 1192 380 1198 390 1200 H0 Z" fill="#9a74c8" opacity=".6"/>

    <g fill="none" stroke="#fff" stroke-width="1.3">
      <circle cx="89" cy="1081" r="10"/>
      <path d="M85 1075 C84 1082 89 1087 95 1087 L96 1084 L93 1082 L91 1084 C89 1083 87 1081 86 1079 L88 1077 L86 1074 Z" fill="#fff" stroke="none"/>
      <circle cx="89" cy="1128" r="10"/>
      <rect x="83" y="1124" width="12" height="8" rx="1"/>
      <path d="M83 1124 L89 1129 L95 1124"/>
    </g>
  </svg>

  <nav class="nav">
    <a href="#">Home</a>
    <a href="#">Contact</a>
    <a href="#" class="active">About</a>
    <a href="#">Product</a>
    <a href="#" class="login">Login</a>
  </nav>

  <div class="abs brand">ZESTOPLEX</div>

  <h1 class="abs hero-title">Making Kids<br>Healthy &amp; Smart</h1>
  <p class="abs hero-copy">Lorem ipsum dolor sit amet, consectetuer adipiscing elit, sed diam nonum. Lorem ipsum dolor sit amet, consectetuer adipiscing elit, sed diam nonum</p>

  <div class="abs hero-art" role="img" aria-label="Illustration of a waving teddy bear holding two vitamin gummy bottles"></div>

  <h2 class="abs about-title">What is<br>Zestoplex ?</h2>
  <a class="abs pill about-more" href="#">Read more</a>
  <p class="abs about-copy">Lorem ipsum dolor sit amet, consectetuer adipiscing elit, sed diam nonum. Lorem ipsum dolor sit amet, consectetuer adipiscing elit, sed diam nonum Lorem ipsum dolor sit amet, consectetuer adipiscing elit, sed diam nonum. Lorem ipsum dolor sit amet, consectetuer adipiscing elit, sed diam nonum</p>

  <p class="abs tagline">Healthy Body<br>Smart<br>Healthy Mind</p>
  <a class="abs pill tag-more" href="#">Read more</a>

  <h2 class="abs product-title">Our Product</h2>
  <p class="abs product-copy">Lorem ipsum dolor sit amet, consectetuer adipiscing elit, sed diam nonum. Lorem ipsum dolor sit amet, consectetuer adipiscing elit, sed diam nonum</p>

  <div class="abs lineup" role="img" aria-label="Row of seven colourful gummy vitamin bottles, the strawberry bottle in front"></div>

  <section class="abs flavour-card">
    <p class="kicker">Strawberry</p>
    <h3>Born<br>to shine</h3>
    <p>Support your brain's learning, concentration and reasoning</p>
  </section>

  <p class="abs flavour-name">STRAWBERRY</p>
  <a class="abs buy" href="#">Buy now</a>

  <div class="abs contact phone">
    <p class="main">+62 (1) 5550 0199</p>
    <p class="sub">Monday-Sunday<br>08.00 AM - 21.00 PM</p>
  </div>
  <div class="abs contact mail">
    <p class="main">noreply@zestoplex.com</p>
    <p class="sub">Monday-Sunday<br>24 HOURS</p>
  </div>

  <div class="abs footer-brand">
    <p class="name">ZESTOPLEX</p>
    <p class="url">www.zestoplex.com</p>
  </div>
  <div class="abs footer-mark"></div>

</main>
</body>
</html>
```